Poster Design Project for Bar in Melbourne

Project Description:
JOB DESCRIPTION:

PROJECT: A1 Poster

We are a popular Beer Hall and Wine Room in Melbourne. www.copperlanebrewhall.com.au We need a poster to promote our up and coming 1st Birthday and we are wanting the look and feel to be like a music festival poster with the head line act and smaller acts being underneath - see example attached. The poster has to be eye catching.
All information below needs to be included - good use of colour!

NAME OF THE EVENT: Copperlanes 1st Birthday! (Headline)

WHATS GOING ON: Opening of Tobbermins, Suckling Pig, 4 new beers on tap, New summer cocktails,

DATE OF EVENT: 2nd December

TIME: Doors open at Midday

ADDRESS: 42 Wexley Rd, Ashcombe
PHONE: 9574-2036
EMAIL: info@copperlanebrewhall.com.au
WEB: www.copperlanebrewhall.com.au

-

IMAGES: Images must be high resolution or vector to ensure clarity and quality is of the highest standard.

POSTER PRODUCTION: Poster must be created in illustrator or photoshop in case any editing needs to be done. Please provide 3mm internal and external bleed
Updates

Update images to be used in the poster design - they are all high res so no need for you to search. Those that I have contacted direct for specific edits please use these images also.

Cheers

Target Market(s)

Demographic is inner city 25 - 45 both men and women, enjoy drinking beer and wine and great food. Social people that love mingling and being out!

Industry/Entity Type

Festival

Requirements
Must have
• Use all imagery below - all are high res quality, poster needs to be eye catching and include company logo etc

```html
<!DOCTYPE html>
<html lang="en">
<head>
<meta charset="utf-8">
<title>Copperlanes 1st Birthday</title>
<link rel="stylesheet" href="https://fonts.googleapis.com/css2?family=Tinos:wght@400;700&display=swap">
<style>
  :root {
    --ink-black: #050505;
    --smoke: #3a3a3a;
    --text-white: #ffffff;
    --brand-pink: #d8587f;
    --bar-red: #e0203a;
    --bar-yellow: #f2e500;
    --bar-green: #3ee040;
    --bar-cyan: #20c8e8;
    --bar-violet: #b030e0;
    --bar-magenta: #ff40c0;
    --bar-orange: #ffa020;
  }
  * { box-sizing: border-box; margin: 0; padding: 0; }
  html, body { width: 847px; height: 1200px; overflow: hidden; background: var(--ink-black); }
  .poster {
    position: relative;
    width: 847px;
    height: 1200px;
    overflow: hidden;
    background: linear-gradient(180deg, var(--ink-black) 0%, #1a1a1a 18%, var(--smoke) 28%, #111 36%, var(--ink-black) 100%);
    font-family: "Tinos", "Times New Roman", serif;
    color: var(--text-white);
  }
  .equalizer-art {
    position: absolute;
    left: 0; top: 340px;
    width: 847px; height: 860px;
    background:
      linear-gradient(180deg, rgba(5,5,5,0.55) 0%, rgba(5,5,5,0.15) 30%, rgba(5,5,5,0.35) 70%, rgba(5,5,5,0.9) 100%),
      linear-gradient(100deg, var(--bar-red) 0%, var(--bar-yellow) 14%, var(--bar-green) 24%, var(--bar-cyan) 34%, var(--bar-violet) 46%, var(--bar-magenta) 58%, var(--bar-orange) 72%, var(--bar-yellow) 84%, var(--bar-green) 100%);
    opacity: 0.8;
  }
  .note {
    position: absolute;
    width: 46px; height: 58px;
    border-radius: 40%;
  }
  .note--green { background: radial-gradient(circle at 35% 35%, #9cff7a, #1a8a1a); }
  .note--gold { background: radial-gradient(circle at 35% 35%, #fff7a0, #c9a400); width: 36px; }
  .note--red { background: radial-gradient(circle at 35% 35%, #ff8080, #a00010); width: 40px; }
  .line { position: absolute; left: 0; width: 847px; text-align: center; white-space: nowrap; }
  .headline { top: 66px; left: 40px; font-size: 55px; font-weight: 400; text-shadow: 0 0 8px #000; }
  .brand-name {
    top: 158px;
    font-size: 104px;
    font-weight: 400;
    letter-spacing: 4px;
    line-height: 1;
    color: var(--brand-pink);
  }
  .brand-sub {
    top: 288px;
    font-size: 42px;
    font-weight: 400;
    letter-spacing: 5px;
    color: var(--brand-pink);
  }
  .brand-rule {
    position: absolute; left: 58px; top: 282px; width: 738px; height: 2px; background: var(--brand-pink);
  }
  .brand-rule--lower { top: 342px; }
  .lineup { font-size: 56px; line-height: 58px; text-shadow: 2px 3px 6px #000, 0 0 10px #000; }
  .lineup-1 { top: 408px; }
  .lineup-2 { top: 466px; }
  .lineup-3 { top: 524px; }
  .lineup-4 { top: 582px; }
  .when { font-size: 50px; text-shadow: 2px 3px 6px #000, 0 0 10px #000; }
  .when-date { top: 728px; }
  .when-time { top: 786px; }
  .contact { font-size: 37px; text-shadow: 2px 2px 5px #000, 0 0 8px #000; }
  .contact-1 { top: 922px; }
  .contact-2 { top: 970px; }
  .contact-3 { top: 1020px; }
  .contact-4 { top: 1068px; }
</style>
</head>
<body>
<div class="poster">
  <div class="equalizer-art" role="img" aria-label="Glowing rainbow-coloured music equalizer bars receding in perspective"></div>

  <div class="note note--green" style="left:32px;top:508px;" role="img" aria-label="Green music note"></div>
  <div class="note note--gold" style="left:760px;top:492px;" role="img" aria-label="Gold music note"></div>
  <div class="note note--gold" style="left:140px;top:712px;" role="img" aria-label="Gold music note"></div>
  <div class="note note--red" style="left:690px;top:705px;" role="img" aria-label="Red treble clef"></div>
  <div class="note note--red" style="left:36px;top:865px;" role="img" aria-label="Red treble clef"></div>
  <div class="note note--green" style="left:755px;top:845px;" role="img" aria-label="Green music note"></div>

  <h1 class="line headline">Copperlanes 1st Birthday!</h1>

  <div class="line brand-name">COPPERLANE</div>
  <div class="brand-rule"></div>
  <div class="line brand-sub">BREW HALL &amp; WINE ROOM</div>
  <div class="brand-rule brand-rule--lower"></div>

  <p class="line lineup lineup-1">Opening of Tobbermins,</p>
  <p class="line lineup lineup-2">Suckling Pig,</p>
  <p class="line lineup lineup-3">4 new beers on tap,</p>
  <p class="line lineup lineup-4">New summer cocktails</p>

  <p class="line when when-date">2nd December</p>
  <p class="line when when-time">Doors open at Midday</p>

  <p class="line contact contact-1">ADDRESS: 42 Wexley Rd, Ashcombe</p>
  <p class="line contact contact-2">PHONE: 9574-2036</p>
  <p class="line contact contact-3">EMAIL: info@copperlanebrewhall.com.au</p>
  <p class="line contact contact-4">WEB: www.copperlanebrewhall.com.au</p>
</div>
</body>
</html>
```